Cash Back to Home Buyers Flyer

We need a flyer for TQ Discount real estate brokerage advertising Money Saving Offer to Home buyers - Cash Back Rebate and explaining how the concept works. The design should communicate how that money saving offer works and should motivate buyers to take advantage of it. Feel free to edit the text based on the attached designs and use infographics.

Target Market(s)

Middle aged professionals

Industry/Entity Type

Real Estate

Requirements
Must have
• Call to action highlights, Dollar signs. Graphics to show rebate math as in the attached file.

```html
<!DOCTYPE html>
<html lang="en">
<head>
<meta charset="utf-8">
<title>Home Buyers Cash Back Rebate Flyer</title>
<link href="https://fonts.googleapis.com/css2?family=Roboto+Condensed:wght@400;700&family=Roboto:wght@400;500;700&family=Lobster+Two:ital,wght@1,700&display=swap" rel="stylesheet">
<style>
  :root{
    --stage:#2a9d94;
    --teal:#17b3a0;
    --teal-dark:#0f8f80;
    --teal-light:#6fd3c4;
    --ink:#3a3a3a;
    --charcoal:#2f2f2f;
    --paper:#ffffff;
    --panel:#f3f4f4;
    --body-text:#555555;
  }
  *{box-sizing:border-box;margin:0;padding:0}
  html,body{width:1200px;height:918px;overflow:hidden;background:var(--stage)}
  .flyer{position:absolute;left:290px;top:21px;width:620px;height:876px;background:var(--paper);overflow:hidden;font-family:'Roboto',sans-serif;box-shadow:0 10px 30px rgba(0,0,0,.25)}
  .top-band{position:absolute;left:0;top:0;width:100%;height:62px;background:var(--teal)}
  .top-band::after{content:"";position:absolute;left:0;bottom:-14px;width:100%;height:14px;background:var(--teal-light)}
  .top-phone{position:absolute;right:26px;top:18px;color:#2e6e67;font:500 21px 'Roboto',sans-serif;display:flex;align-items:center;gap:8px}
  .brand{position:absolute;left:34px;top:110px;display:flex;align-items:center;gap:8px;color:#7a7a7a;font:500 17px 'Roboto',sans-serif}
  .brand-mark{width:14px;height:14px;background:var(--teal)}
  .hero{position:absolute;left:0;top:70px;width:620px;height:360px}
  .hero-title{position:absolute;left:20px;top:272px}
  .hero-title span{display:block;width:max-content;font:700 28px 'Roboto Condensed',sans-serif;letter-spacing:.5px;padding:3px 12px;margin-bottom:8px}
  .hero-title .line-one{background:var(--teal);color:#fff}
  .hero-title .line-two{background:#fff;color:var(--teal)}
  .hero-tagline{position:absolute;left:22px;top:368px;width:330px;color:#fff;font:700 12.5px 'Roboto',sans-serif;line-height:1.3}
  .hero-offer{position:absolute;right:22px;top:360px;display:flex;align-items:center;gap:8px;color:#fff}
  .hero-offer .pill{border:2px solid #fff;border-radius:20px;padding:2px 10px;font:700 18px 'Roboto Condensed',sans-serif}
  .hero-offer .big{font:700 46px 'Roboto Condensed',sans-serif}
  .web-bar{position:absolute;left:70px;top:446px;width:480px;height:28px;background:#4a4a4a;color:#eee;font:400 14px 'Roboto',sans-serif;display:flex;align-items:center;justify-content:center}
  .rebate-box{position:absolute;left:22px;top:490px;width:576px;height:212px;background:var(--panel);border-radius:26px;box-shadow:0 6px 16px rgba(0,0,0,.12);padding:18px 20px;color:var(--body-text);font:400 16.5px 'Roboto Condensed',sans-serif;text-transform:uppercase;text-align:center}
  .rebate-line{display:block;height:35px;line-height:35px;white-space:nowrap}
  .rebate-line.closing{font-size:19px;font-weight:700;color:var(--ink)}
  .hl-tag{background:var(--teal);color:#fff;font-weight:700;padding:2px 8px}
  .hl-text{color:var(--teal)}
  .hl-amount{display:inline-block;line-height:1;vertical-align:middle;background:#fff;color:var(--teal-dark);font-weight:700;font-size:27px;padding:2px 8px;box-shadow:0 2px 6px rgba(0,0,0,.12)}
  .hl-amount sup{font-size:14px}
  .disclaimer{position:absolute;left:0;top:722px;width:620px;height:110px;background:var(--teal);border-radius:34px 34px 0 0;padding:16px 30px;color:#0d3d37;font:700 italic 17px/1.4 'Lobster Two',sans-serif;text-align:center}
  .footer{position:absolute;left:0;top:790px;width:620px;height:86px;background:var(--charcoal);color:#ddd;display:flex;justify-content:space-between;align-items:flex-start;padding:10px 28px;font:400 12px/1.45 'Roboto',sans-serif}
  .footer h3{font:700 italic 15px 'Lobster Two',sans-serif;color:#fff;margin-bottom:1px}
  .footer .brand-footer{display:flex;align-items:center;gap:7px;color:#eee;font:500 15px 'Roboto',sans-serif;margin-top:20px}
  .footer .brand-footer i{width:12px;height:12px;background:var(--teal);display:block}
</style>
</head>
<body>
<main class="flyer">
  <div class="top-band">
    <div class="top-phone">
      <svg width="18" height="18" viewBox="0 0 24 24"><path d="M6.6 10.8a15 15 0 0 0 6.6 6.6l2.2-2.2c.3-.3.7-.4 1-.2 1.1.4 2.3.6 3.6.6.6 0 1 .4 1 1V20c0 .6-.4 1-1 1A17 17 0 0 1 3 4c0-.6.4-1 1-1h3.5c.6 0 1 .4 1 1 0 1.3.2 2.5.6 3.6.1.3 0 .7-.2 1z" fill="none" stroke="#2e6e67" stroke-width="2"/></svg>
      (555) 014-2290
    </div>
  </div>

  <svg class="hero" viewBox="0 0 620 360" role="img" aria-label="Photo of a large illuminated luxury home with landscaped front garden at dusk">
    <defs>
      <linearGradient id="heroPhoto" x1="0" y1="0" x2="0" y2="1">
        <stop offset="0" stop-color="#c9dbe8"/>
        <stop offset=".45" stop-color="#7f95ad"/>
        <stop offset=".75" stop-color="#5b7f5a"/>
        <stop offset="1" stop-color="#2f6a4c"/>
      </linearGradient>
      <linearGradient id="heroFade" x1="0" y1="0" x2="1" y2="0">
        <stop offset=".55" stop-color="#17b3a0" stop-opacity="0"/>
        <stop offset="1" stop-color="#17b3a0" stop-opacity=".85"/>
      </linearGradient>
    </defs>
    <path d="M0 160 H150 Q205 160 205 110 V60 Q205 10 255 10 H620 V360 H0 Z" fill="url(#heroPhoto)"/>
    <path d="M0 300 H620 V360 H0 Z" fill="url(#heroFade)"/>
    <g fill="none" stroke="#fff" stroke-width="2" font-family="Roboto Condensed, sans-serif" font-weight="700" font-size="90">
      <text x="400" y="130">$</text>
      <text x="470" y="110">$</text>
      <text x="420" y="250">$</text>
      <text x="490" y="230">$</text>
    </g>
  </svg>

  <div class="brand"><span class="brand-mark"></span>Harbor Key Realty</div>

  <div class="hero-title">
    <span class="line-one">HOME BUYERS</span>
    <span class="line-two">CASH BACK REBATE</span>
  </div>
  <p class="hero-tagline">If you are buying or planning to buy a property in NJ this information can make a big difference for you.</p>
  <div class="hero-offer"><span class="pill">UP TO</span><span class="big">2%</span></div>

  <div class="web-bar">Visit our website for more info: www.harborkeyrealty.net</div>

  <section class="rebate-box">
    <span class="rebate-line">You can get <span class="hl-tag">UP TO 2%</span> of <span class="hl-text">selling price back</span> in your pocket</span>
    <span class="rebate-line">at closing. Average rebate we pay for a $500,000 home sale</span>
    <span class="rebate-line">is about <span class="hl-amount"><sup>$</sup>7,500!</span> The same great level of service,</span>
    <span class="rebate-line">professional advice and guidance <span class="hl-tag">PLUS</span> a huge check</span>
    <span class="rebate-line closing">at your closing to cover your closing costs!</span>
  </section>

  <div class="disclaimer">All commissions are negotiable in NJ.<br>Consult a tax professional regarding a receipt of the rebate.</div>

  <footer class="footer">
    <div class="footer-contact">
      <h3>Contact Us Today!</h3>
      Phone: (555) 014-2290<br>
      Office: (555) 017-4410<br>
      Email: hello@harborkeyrealty.net
    </div>
    <div class="footer-address">
      <h3>Come Have a Coffee With Us!</h3>
      Harbor Key Realty LLC.<br>
      1480 Meadow Road, Suite 210<br>
      Brookfield, NJ 07000
    </div>
    <div class="brand-footer"><i></i>Harbor Key Realty</div>
  </footer>
</main>
</body>
</html>
```